Pathways to Brightmoor Land Ventures

size of the ad - 8”x 10.75" plus 0.25" bleed
I would like an ad for a magazine that will stand out and make people want to read the ad.
The ad should not be crowded and people reading the ad will be able to read the text.
I would like it to be a creative and modern-day design.
the list of topics should not be the focus of the ad.
the text is attached.
If you decide to use people in the ad then please no ladies.
please note that leave over 1 inch for the bottom of the footer

```html
<!DOCTYPE html>
<html lang="en">
<head>
<meta charset="utf-8">
<title>Real Estate Course – Pathways to Brightmoor Land Ventures</title>
<link href="https://fonts.googleapis.com/css2?family=Bebas+Neue&family=Roboto+Condensed:wght@400;700&family=Roboto:wght@400&display=swap" rel="stylesheet">
<style>
  :root {
    --navy: #07446e;
    --navy-mid: #1d5680;
    --navy-soft: #7f9fb8;
    --ink: #231f20;
    --white: #ffffff;
    --footer-grey: #e5e6e7;
  }
  * { margin: 0; padding: 0; box-sizing: border-box; }
  html, body { width: 942px; height: 1200px; overflow: hidden; background: var(--white); }
  .ad {
    position: relative;
    width: 942px;
    height: 1200px;
    overflow: hidden;
    background: linear-gradient(180deg,
      var(--navy) 0%,
      var(--navy) 28%,
      var(--navy-mid) 45%,
      var(--navy-soft) 62%,
      #c6d4df 72%,
      var(--white) 80%,
      var(--white) 100%);
    font-family: "Roboto Condensed", "Arial Narrow", sans-serif;
  }
  .ad__title {
    position: absolute;
    top: 34px; left: 0; width: 100%;
    text-align: center;
    font-family: "Bebas Neue", Impact, sans-serif;
    font-size: 124px;
    line-height: 1;
    letter-spacing: 1px;
    color: var(--white);
  }
  .ad__skyline {
    position: absolute;
    top: 165px; left: 126px;
    width: 693px; height: 528px;
  }
  .ad__headline {
    position: absolute;
    top: 724px; left: 0; width: 100%;
    text-align: center;
    font-family: "Bebas Neue", Impact, sans-serif;
    font-size: 76px;
    line-height: 0.88;
    color: var(--navy);
  }
  .ad__tagline {
    position: absolute;
    top: 872px; left: 0; width: 100%;
    text-align: center;
    font-size: 37px;
    line-height: 1.1;
    color: var(--ink);
    text-transform: uppercase;
  }
  .ad__tagline strong { color: var(--navy); font-weight: 700; }
  .label {
    font-size: 13px;
    font-weight: 700;
    line-height: 16px;
    color: var(--ink);
  }
  .topics { position: absolute; top: 963px; left: 76px; }
  .topics__list { list-style: none; font-size: 13.5px; line-height: 17px; color: var(--ink); }
  .topics__list li { position: relative; padding-left: 11px; white-space: nowrap; }
  .topics__list li::before {
    content: ""; position: absolute; left: 0; top: 7px;
    width: 5px; height: 5px; border-radius: 50%; background: var(--ink);
  }
  .topics__list--main { margin-top: 8px; }
  .topics__list--extra { position: absolute; top: 1005px; left: 294px; }
  .location { position: absolute; top: 971px; left: 467px; }
  .schedule {
    position: absolute;
    top: 994px; left: 467px;
    width: 160px; height: 93px;
    background: var(--navy);
    color: var(--white);
    padding: 10px 0 0 10px;
    font-size: 15px;
    line-height: 19px;
  }
  .schedule__start { font-size: 20px; margin-top: 7px; display: block; }
  .perks { position: absolute; top: 994px; left: 636px; list-style: none; }
  .perks li {
    display: flex; align-items: center; gap: 5px;
    font-size: 17px; font-weight: 700; color: var(--navy);
    line-height: 22px; margin-bottom: 5px;
    white-space: nowrap;
  }
  .perks svg { width: 14px; height: 14px; flex: none; }
  .audience {
    position: absolute; top: 1055px; left: 656px;
    font-family: "Roboto", Arial, sans-serif;
    font-size: 12.5px; line-height: 16px; color: var(--ink);
  }
  .footer-band {
    position: absolute; left: 0; bottom: 0;
    width: 100%; height: 85px;
    background: var(--footer-grey);
  }
</style>
</head>
<body>
<main class="ad">
  <h1 class="ad__title">Real Estate Course</h1>

  <svg class="ad__skyline" role="img" aria-label="Line-art illustration of a city skyline with office towers, trees, clouds and sun" viewBox="0 0 693 528">
    <defs>
      <linearGradient id="skyline-tone" x1="0" y1="0" x2="0" y2="1">
        <stop offset="0" stop-color="#ffffff" stop-opacity="0.16"/>
        <stop offset="1" stop-color="#ffffff" stop-opacity="0.9"/>
      </linearGradient>
    </defs>
    <rect x="0" y="0" width="693" height="528" rx="6" fill="url(#skyline-tone)"/>
  </svg>

  <h2 class="ad__headline">Pathways to Brightmoor<br>Land Ventures</h2>

  <p class="ad__tagline">Investing in <strong>knowledge</strong> is<br>investing in <strong>opportunities.</strong></p>

  <section class="topics">
    <h3 class="label">TOPICS:</h3>
    <ul class="topics__list topics__list--main">
      <li>Partial listing</li>
      <li>Real estate investment strategies</li>
      <li>Due diligence</li>
      <li>Financing</li>
      <li>Underwriting</li>
      <li>Property management</li>
    </ul>
  </section>
  <ul class="topics__list topics__list--extra">
    <li>Real estate Legal basics</li>
    <li>Sourcing deals</li>
    <li>Syndication</li>
    <li>Dealing with brokers</li>
    <li>Tax fundamentals</li>
  </ul>

  <h3 class="label location">ELM HOLLOW</h3>
  <div class="schedule">
    10 -TUESDAY<br>EVENINGS SESSIONS
    <span class="schedule__start">Starting Feb.28</span>
  </div>

  <ul class="perks">
    <li><svg viewBox="0 0 14 14"><path d="M1.5 7.5 L5 11 L12.5 2.5" fill="none" stroke="#07446e" stroke-width="2.4" stroke-linecap="round" stroke-linejoin="round"/></svg>Limited Partial Scholarships</li>
    <li><svg viewBox="0 0 14 14"><path d="M1.5 7.5 L5 11 L12.5 2.5" fill="none" stroke="#07446e" stroke-width="2.4" stroke-linecap="round" stroke-linejoin="round"/></svg>Early Bird Special</li>
  </ul>
  <p class="audience">For those that started or<br>would like to go into real estate</p>

  <div class="footer-band"></div>
</main>
</body>
</html>
```